independent cleaner, reliable, custom, thorough, trustworthy

Not sure yet if I want single-sided or double sided, so I'm selecting double-sided just in case, but single-sided designs are okay.

Really looking to find the happy medium between personal and professional in a business card design. I end up building comfortable relationships with the people I work for.

Most of my business is through referrals, but I want some business cards to hand out to people who ask for one (and maybe put them on community bulletin boards).

My target market is homeowners and business owners who are looking for a reliable cleaner and are willing to pay a bit more to have excellent quality and someone they trust.

Theme: I have a personal-professional feel since I'm solo, so the theme should reflect that. Trustworthy, personal, simple. I clean up messes.

Hopefully this is enough info, let me know if you have any questions though of course!

Target Market(s)

Homeowners businessowners who are looking for a reliable cleaner, excellent quality trustworthy.

Industry/Entity Type

Cleaning Service

Contact Information for Business Card

Please include this text:
• Delphine Marrow
• independent cleaner
• reliable, custom, thorough
• 604-317-2296
• tbw.marrow@quillpost.net

Font styles to use
Serif
Sans Serif

Colors
ffffff
00a990
0492cd
33a6d7
0355a3
3276b5
919191

Requirements
Must have
• Really looking to find the happy medium between personal and professional in a business card design.
• Background: at least 50% white on the side with the most text (coloured accents or shapes are okay)
• I lean more towards simple and clean, solid colours, maybe a gentle gradient
Nice to have
• Not sure yet if I want single-sided or double sided, so I'm selecting double-sided just in case, but single-sided designs are okay.
• Colours: preferably blues and teals for the font and other objects (if any). Open to designer's choice though. I've toyed around with orangey-yellow, but it doesn't feel right and I keep going back to blues/teals
• Also I uploaded a sketch of my signature and initials so you can get a feel for my personality. I'm not expecting this to be included in the design, it's just there.
Should not have
• I don't like a lot of busy-ness or textures
• Also I don't have a logo (not sure where else to specify this)

```html
<!DOCTYPE html>
<html lang="en">
<head>
<meta charset="utf-8">
<title>Delphine Marrow – Independent Cleaner Business Card</title>
<link rel="stylesheet" href="https://fonts.googleapis.com/css2?family=Montserrat:wght@300;400;500&family=Great+Vibes&display=swap">
<style>
  :root {
    --page-bg: #e9ecef;
    --card-white: #ffffff;
    --card-blue: #0f72b8;
    --blue-deep: #0355a3;
    --blue-mid: #3276b5;
    --blue-bright: #0492cd;
    --blue-light: #33a6d7;
    --shadow: rgba(20, 40, 70, 0.16);
  }
  * { box-sizing: border-box; margin: 0; padding: 0; }
  html, body {
    width: 1200px;
    height: 960px;
    overflow: hidden;
    background: var(--page-bg);
  }
  .sheet {
    width: 1200px;
    height: 960px;
    display: flex;
    flex-direction: column;
    align-items: center;
    justify-content: center;
    gap: 56px;
  }
  .card {
    width: 700px;
    height: 400px;
    border-radius: 4px;
    box-shadow: 0 10px 30px var(--shadow);
    position: relative;
    overflow: hidden;
  }

  /* Back side */
  .card--back {
    background: var(--card-blue);
    display: flex;
    align-items: center;
    justify-content: center;
  }
  .card--back .wordmark {
    color: var(--card-white);
    font-size: 84px;
  }

  /* Shared wordmark */
  .wordmark {
    font-family: "Montserrat", sans-serif;
    font-weight: 500;
    letter-spacing: 1px;
    line-height: 1;
  }

  /* Front side */
  .card--front {
    background: var(--card-white);
  }
  .card--front .wordmark {
    position: absolute;
    left: 48px;
    top: 150px;
    font-size: 62px;
    color: var(--blue-deep);
  }
  .divider {
    position: absolute;
    left: 348px;
    top: 96px;
    width: 2px;
    height: 190px;
    background: linear-gradient(to bottom, rgba(4,146,205,0), var(--blue-bright) 45%, rgba(4,146,205,0));
  }
  .details {
    position: absolute;
    left: 376px;
    top: 92px;
    width: 300px;
  }
  .details__name {
    font-family: "Great Vibes", cursive;
    font-size: 40px;
    line-height: 1;
    color: var(--blue-light);
  }
  .details__role {
    font-family: "Montserrat", sans-serif;
    font-weight: 300;
    font-size: 19px;
    color: var(--blue-mid);
    margin-top: 4px;
  }
  .contact {
    list-style: none;
    margin-top: 10px;
  }
  .contact__item {
    display: flex;
    align-items: center;
    gap: 10px;
    font-family: "Montserrat", sans-serif;
    font-weight: 300;
    font-size: 17px;
    color: var(--blue-mid);
    line-height: 1.55;
  }
  .contact__icon {
    width: 15px;
    height: 15px;
    flex: none;
    fill: var(--blue-bright);
  }
  .values {
    margin-top: 16px;
    font-family: "Great Vibes", cursive;
    font-size: 24px;
    color: var(--blue-deep);
    display: flex;
    align-items: center;
    gap: 10px;
  }
  .values__dot {
    width: 7px;
    height: 7px;
    border-radius: 50%;
    background: var(--blue-bright);
  }
</style>
</head>
<body>
<main class="sheet">
  <section class="card card--back" aria-label="Card back">
    <span class="wordmark">Marrow</span>
  </section>

  <section class="card card--front" aria-label="Card front">
    <span class="wordmark">Marrow</span>
    <div class="divider"></div>
    <div class="details">
      <p class="details__name">Delphine Marrow</p>
      <p class="details__role">Independent Cleaner</p>
      <ul class="contact">
        <li class="contact__item">
          <svg class="contact__icon" viewBox="0 0 24 24" aria-hidden="true">
            <path d="M6.6 10.8a15.1 15.1 0 0 0 6.6 6.6l2.2-2.2a1 1 0 0 1 1-.25 11.4 11.4 0 0 0 3.6.57 1 1 0 0 1 1 1V20a1 1 0 0 1-1 1A17 17 0 0 1 3 4a1 1 0 0 1 1-1h3.5a1 1 0 0 1 1 1c0 1.25.2 2.45.57 3.57a1 1 0 0 1-.25 1z"/>
          </svg>
          604-317-2296
        </li>
        <li class="contact__item">
          <svg class="contact__icon" viewBox="0 0 24 24" aria-hidden="true">
            <path d="M2 5h20v14H2z M3.5 6.5 12 13l8.5-6.5" fill="none" stroke="#0492cd" stroke-width="2"/>
          </svg>
          tbw.marrow@quillpost.net
        </li>
      </ul>
      <p class="values">
        <span>Reliable</span><span class="values__dot"></span>
        <span>Custom</span><span class="values__dot"></span>
        <span>Thorough</span>
      </p>
    </div>
  </section>
</main>
</body>
</html>
```